Massage Therapy and Energy Healing Practice

I am a massage therapist, Reiki energy healer, I sell herbs and oils, and also a health lifestyle coach. I need a design that is strong because I'm not a spa. I do therapeutic work, but I want a touch of the energy and spiritual healing I do as well to be included in the design. I like blue, green, or purple colors. I live in the Blue Ridge Mountains of VA and even though my practice is in the city I like my love for nature and the earth to show through. I would like a single image logo so I can use the image many places. I need a strong brand that will let others know that I combine massage therapy in a therapeutic way while keeping my touches of energy healing, nurturing, herb crafting, and mother earth loving ways.
Updates

Just some things about me:I like to hike. I live on a farm. I own horses, cows, sheep and dogs. I love nature and the energy in produces. I'm very spiritual. I don't know how these things might help or if they do, but I know that my personality might help inspire what I will find good in a design. Added Sunday, December 13, 2015

Target Market(s)

People in pain. People who need spiritual council. Need herbal medicine advice. Holistic healthcare.

Industry/Entity Type

Massage

Contact Information for Business Card

Kneadwell Harbor
Norah T. Lindqvist C.M.T, R.M.T
40913 Hollister Creek Court, Dunmore, VA
540-718-2263

Colors
3176b5
85abd2
876aae
9bcb3c

Requirements
Must have
• Strong Branding that promotes my massage therapy practice first
Nice to have
• Something to evoke my herbal medicine, my energy healing, my spiritual side

```html
<!DOCTYPE html>
<html lang="en">
<head>
<meta charset="utf-8">
<title>Kneadwell Harbor – Business Card</title>
<link rel="stylesheet" href="https://fonts.googleapis.com/css2?family=Bodoni+Moda:wght@500&family=Open+Sans:wght@400&display=swap">
<style>
  :root {
    --page-bg: #e9e7e3;
    --card-blue: #2f73b4;
    --band-black: #111111;
    --rule-white: #f4f6f8;
    --photo-light: #a59d94;
    --photo-mid: #7d756d;
    --photo-dark: #5b524c;
    --title-ink: #0c0c0c;
    --text-white: #ffffff;
  }
  * { margin: 0; padding: 0; box-sizing: border-box; }
  html, body {
    width: 1200px; height: 902px; overflow: hidden;
    background: var(--page-bg);
  }
  .canvas {
    width: 1200px; height: 902px;
    display: flex; align-items: center; justify-content: center;
  }
  .business-card {
    position: relative;
    width: 1000px; height: 572px;
    background: var(--card-blue);
    box-shadow: 0 6px 22px rgba(0,0,0,0.18);
    overflow: hidden;
  }
  .card-art {
    position: absolute; inset: 0;
    width: 100%; height: 100%;
  }
  .brand-name {
    position: absolute;
    left: 0; right: 0; top: 168px;
    text-align: center;
    font-family: "Bodoni Moda", "Didot", serif;
    font-weight: 500;
    font-size: 92px;
    letter-spacing: 1px;
    color: var(--title-ink);
    line-height: 1;
  }
  .contact-block {
    position: absolute;
    left: 0; right: 0; top: 392px;
    text-align: center;
    font-family: "Open Sans", "Segoe UI", sans-serif;
    color: var(--text-white);
  }
  .person-name { font-size: 34px; line-height: 1.1; margin-left: 40px; }
  .credentials { font-size: 19px; letter-spacing: 1px; margin-top: 2px; margin-left: 60px; }
  .phone { font-size: 24px; margin-top: 30px; letter-spacing: 1px; }
  .address { font-size: 24px; margin-top: 14px; letter-spacing: 0.5px; }
</style>
</head>
<body>
<main class="canvas">
  <section class="business-card">
    <svg class="card-art" viewBox="0 0 1000 572" preserveAspectRatio="none">
      <defs>
        <linearGradient id="farmTones" x1="0" y1="0" x2="1" y2="1">
          <stop offset="0" stop-color="var(--photo-light)"/>
          <stop offset="0.55" stop-color="var(--photo-mid)"/>
          <stop offset="1" stop-color="var(--photo-dark)"/>
        </linearGradient>
      </defs>
      <polygon class="rule-white" fill="var(--rule-white)"
        points="0,0 1000,0 1000,322 872,384 128,384 0,338"/>
      <polygon class="band-black" fill="var(--band-black)"
        points="0,0 1000,0 1000,312 868,372 132,372 0,328"/>
      <polygon class="farm-photo" fill="url(#farmTones)"
        role="img" aria-label="Photo of a cow and a flock of sheep behind a wire fence on a farm field"
        points="0,0 1000,0 1000,300 864,356 136,356 0,316"/>
    </svg>
    <h1 class="brand-name">Kneadwell Harbor</h1>
    <div class="contact-block">
      <p class="person-name">Norah T. Lindqvist</p>
      <p class="credentials">C.M.T, R.M.T</p>
      <p class="phone">540-718-2263</p>
      <p class="address">40913 Hollister Creek Court, Dunmore, VA</p>
    </div>
  </section>
</main>
</body>
</html>
```